MCP phase 1 web design

Meridale Capital Partners Ltd (MCP) is a challenger business to the traditional leasing market. We look for solutions to complex problems involving the funding of capital equipment within an office environment and then build documentation around the solution. We recently created a brief for a logo and successfully completed that assignment. We now need to create our first web site which is simply intended to be informative. To help interested designers we have attached a detailed brief that is broken into three sections. The first explains how we see the site developing over time from something quite straightforward initially to a full transaction capability. Whoever wins this competition will be expected to work with us into the future to help develop the site. Section 2 gives you a view about our likes and dislikes by reviewing some existing sites. Section 3 gives you the structure and content of the site based upon our likes and dislikes. We are by no means committed to the structure and if you believe it can be presented in a better way then please use your design. The text is fixed as content. The images to appear can be anything from photographs to line drawings again entirely at the designers whim. Currently we have a home page plus 5 subsidiary pages. A few things to help you:
1. The logo is fixed and should be amongst the downloads.
2. The colours we have are corporate and should be used.
3. The typeface we use within the business is "Verdana"
Good luck.

Industry/Entity Type

Business

```html
<!DOCTYPE html>
<html lang="en">
<head>
<meta charset="utf-8">
<title>Managed Services Solutions – Meridale Capital Partners Ltd</title>
<link rel="stylesheet" href="https://fonts.googleapis.com/css2?family=Noto+Sans:wght@400&display=swap">
<style>
  :root {
    --brand-blue: #1a6fb5;
    --nav-grey: #555;
    --menu-grey: #575757;
    --panel-blue: #2286dc;
    --panel-blue-dark: #1c6fc0;
    --page-light: #f2f2f2;
    --page-dark: #dcdcdc;
    --white: #fff;
  }
  * { margin: 0; padding: 0; box-sizing: border-box; }
  html, body { width: 1200px; height: 1000px; overflow: hidden; }
  body {
    position: relative;
    font-family: Verdana, "Noto Sans", sans-serif;
    background: var(--white);
  }
  .page-backdrop {
    position: absolute; left: 0; top: 0; width: 1200px; height: 898px;
    background: radial-gradient(ellipse 700px 600px at 600px 380px, var(--page-light), var(--page-dark));
  }
  .site-header {
    position: absolute; left: 0; top: 0; width: 1200px; height: 68px;
    background: var(--white);
    border-top: 5px solid var(--brand-blue);
    box-shadow: 0 2px 3px rgba(0,0,0,.45);
    z-index: 2;
  }
  .brand {
    position: absolute; left: 112px; top: 20px;
    display: flex; align-items: center; gap: 10px;
    color: var(--brand-blue); font-size: 19px; letter-spacing: .5px;
  }
  .brand-square { width: 22px; height: 22px; background: var(--brand-blue); }
  .main-nav a {
    position: absolute; top: 26px;
    color: var(--nav-grey); font-size: 17px; text-decoration: none; letter-spacing: .3px;
  }
  .main-nav .current { color: var(--brand-blue); }
  .solutions-menu {
    position: absolute; left: 755px; top: 69px; width: 248px; height: 111px;
    background: var(--menu-grey); border-radius: 6px;
    box-shadow: 2px 3px 5px rgba(0,0,0,.4);
    z-index: 3; padding-top: 17px;
  }
  .solutions-menu::before {
    content: ""; position: absolute; left: 104px; top: -12px;
    border: 7px solid transparent; border-bottom: 6px solid var(--menu-grey);
  }
  .solutions-menu a {
    display: block; margin: 0 8px 0 7px; height: 25px; line-height: 25px;
    padding-left: 5px; margin-bottom: 4px;
    color: var(--white); font-size: 16px; text-decoration: none;
  }
  .solutions-menu .active { background: var(--brand-blue); }
  .content-card {
    position: absolute; left: 100px; top: 82px; width: 1000px; height: 574px;
    background: var(--white); border-radius: 8px; overflow: hidden;
  }
  .page-title {
    position: absolute; left: 10px; top: 20px;
    color: var(--brand-blue); font-size: 32px; font-weight: 400; letter-spacing: .5px;
  }
  .hero-image {
    position: absolute; left: 1px; top: 68px; width: 571px; height: 341px;
    background: linear-gradient(90deg, #2e5f70 0%, #1a2f48 45%, #0b1530 100%);
  }
  .intro-panel {
    position: absolute; left: 572px; top: 68px; width: 429px; height: 341px;
    background: radial-gradient(ellipse at 60% 20%, #2f95ea, var(--panel-blue-dark));
    overflow: hidden;
  }
  .intro-text {
    position: absolute; left: 12px; top: 21px; width: 385px;
    color: var(--white); font-size: 15.2px; line-height: 17.5px;
  }
  .intro-text p { margin-bottom: 17.5px; }
  .scrollbar { position: absolute; left: 405px; top: 6px; }
</style>
</head>
<body>
  <div class="page-backdrop"></div>

  <header class="site-header">
    <div class="brand"><span class="brand-square"></span><span>MERIDALE CAPITAL PARTNERS LTD</span></div>
    <nav class="main-nav">
      <a href="#" style="left:498px">HOME</a>
      <a href="#" style="left:602px">WHY ALTERNATIVE?</a>
      <a href="#" class="current" style="left:822px">SOLUTIONS ▾</a>
      <a href="#" style="left:1005px">CONTACT</a>
    </nav>
  </header>

  <nav class="solutions-menu">
    <a href="#" class="active">Managed Services</a>
    <a href="#">Public Sector</a>
    <a href="#">Education</a>
  </nav>

  <main class="content-card">
    <h1 class="page-title">Managed Services Solutions</h1>
    <div class="hero-image" role="img" aria-label="Businessman drawing a cloud network sketch with connected device icons"></div>
    <section class="intro-panel">
      <div class="intro-text">
        <p>Large enterprises, as well as SMEs, not-for profit and most Public Sector organisations, ask for flexibility as a key requirement for any technology implementation. They are well aware that their needs will keep evolving over the lifetime of the technology they chose to implement and therefore ask for a contractual and financing approach to meet those ever changing needs.</p>
        <p>A typical example would be the deployment, service and overall management of a fleet of print output devices, perhaps integrated into a document management system or complete IT system.</p>
        <p>A traditional lease, even in some of the more innovative forms, is not enough to provide the flexibility that these customers require.</p>
      </div>
      <svg class="scrollbar" width="12" height="330" viewBox="0 0 12 330" aria-hidden="true">
        <rect x="0" y="0" width="12" height="330" fill="#3a9bf0"/>
        <path d="M3 6 L6 3 L9 6" stroke="#fff" stroke-width="1.5" fill="none"/>
        <rect x="1" y="13" width="10" height="19" rx="4" fill="#8fc4f5"/>
        <path d="M3 323 L6 326 L9 323" stroke="#fff" stroke-width="1.5" fill="none"/>
      </svg>
    </section>
  </main>
</body>
</html>
```